Design for a creative video production company !!

Looking for a 3-4 page layout for my project proposals. Should include :
Cover page
Page 1: is the general overview (see attached)
Page 2: Project Outline ( a blank area to add project specifics)
Page 3: budget (a blank table here I can add in the numbers)

final version a pdf I can edit. even just a page design I can add as my background. More info on company please go to www.brightmarlowfilms.com

Target Market(s)

Marketing managers, communications people, people who want to use video ... professional video to tell their story or educate.

Industry/Entity Type

It Company

Font styles to use
Serif
Sans Serif

Colors

Designer to choose colors to be used in the design.

Requirements
Must have
• Must have a way I can fill in the information later, I'm happy to use a background and leave an area black I can add a table for budgets. Would like to see a pie chart or graph used to show the time of each stage of the project. See general overview doc attached.
Nice to have
• A variation of the proposal I attached is just a start, Please look at website, (brightmarlowfilms.com) business cards, and proposal as an idea of the branding.
Should not have
• sad clowns

```html
<!DOCTYPE html>
<html lang="en">
<head>
<meta charset="utf-8">
<title>Bright Marlow Films – Proposal Booklet</title>
<link href="https://fonts.googleapis.com/css2?family=Open+Sans:wght@400;600;700;800&display=swap" rel="stylesheet">
<style>
  :root{
    --red:#8c1f26;
    --red-dark:#6a151b;
    --ink:#2f2f33;
    --ink-soft:#55565b;
    --paper:#f4f4f5;
    --panel:#2c2c30;
    --stage:#2a2a2a;
    --rule:#b9b9bd;
  }
  *{box-sizing:border-box;margin:0;padding:0}
  html,body{width:850px;height:1200px;overflow:hidden}
  body{background:var(--stage);font-family:"Open Sans",Arial,sans-serif;color:var(--ink);position:relative}

  .spread{position:absolute;left:85px;width:680px;height:480px;display:flex}
  .spread--front{top:40px}
  .spread--inside{top:610px}
  .page{position:relative;width:340px;height:480px;overflow:hidden}
  .spread-label{position:absolute;color:#fff;font-size:48px;font-weight:400;letter-spacing:.5px}
  .spread-label--front{top:525px;left:545px}
  .spread-label--inside{top:1100px;left:150px}

  .fold-tabs{position:absolute;left:328px;top:0;width:24px;height:480px;pointer-events:none}
  .fold-tab{position:absolute;left:0;width:24px;height:30px;background:linear-gradient(90deg,var(--red-dark) 0 50%,var(--red) 50% 100%)}

  .shape-layer{position:absolute;inset:0;width:100%;height:100%}

  /* Brand name */
  .brand{position:absolute;line-height:1;font-weight:800;font-size:14px;letter-spacing:.3px;text-transform:uppercase;display:flex;align-items:center;gap:5px;white-space:nowrap}
  .brand__dot{width:7px;height:7px;background:var(--red);display:inline-block}

  /* Back cover */
  .back-cover{background:#ddd}
  .back-cover__photo{position:absolute;inset:0;background:linear-gradient(160deg,#d9d9dc 0%,#9d9ea3 45%,#c7c7ca 70%,#e4e4e6 100%)}
  .back-cover .brand{left:112px;top:264px;color:var(--red)}
  .contact{position:absolute;left:178px;top:300px;color:var(--red)}
  .contact__title{font-size:11px;font-weight:600;margin-bottom:6px}
  .contact__row{display:flex;align-items:flex-start;gap:6px;font-size:7.5px;margin-bottom:7px;line-height:1.3}
  .contact__icon{width:11px;height:11px;flex:none}

  /* Front cover */
  .front-cover{background:var(--panel)}
  .front-cover__photo{position:absolute;left:0;top:48px;width:340px;height:260px;background:linear-gradient(120deg,#3a3c42 0%,#6b6e76 35%,#c9c9cc 70%,#ededee 100%)}
  .front-cover__header{position:absolute;left:0;top:0;width:340px;height:48px;background:var(--panel)}
  .front-cover .brand{left:30px;top:17px;color:#fff}
  .cover-pitch{position:absolute;left:118px;top:262px;width:205px;color:#fff}
  .cover-pitch__title{font-size:21px;font-weight:800;line-height:1.05;text-transform:uppercase;margin-bottom:10px}
  .cover-pitch__text{font-size:9.5px;line-height:1.35;color:#e6e6e8;padding-bottom:6px;border-bottom:1px solid #8a8a8e;width:160px}
  .cover-url{position:absolute;right:18px;top:402px;color:#fff;font-size:8px;font-weight:700}

  /* Inside pages */
  .inside-page{background:var(--paper);padding:16px 18px}
  .inside-page .brand{color:var(--ink);right:18px;top:18px}
  .page-url{position:absolute;right:20px;bottom:16px;font-size:8.5px;font-weight:700;color:var(--ink-soft)}
  .section-title{color:var(--red);font-size:11px;font-weight:700;margin-bottom:3px}
  .body-copy{font-size:5.6px;line-height:1.45;color:var(--ink-soft)}
  .overview{position:absolute;left:18px;top:42px;width:300px}
  .overview .body-copy{margin-bottom:8px}
  .stage{margin-bottom:9px}
  .stage__title{color:var(--red);font-size:8.5px;font-weight:700;margin-bottom:2px}
  .tick-list{list-style:none}
  .tick-list li{display:flex;gap:4px;font-size:5.6px;line-height:1.4;color:var(--ink-soft);margin-bottom:1px}
  .tick-list b{color:var(--ink);font-weight:700}
  .tick{width:6px;height:6px;flex:none;margin-top:1px}
  .stage__note{font-size:5.4px;color:var(--ink-soft);padding-left:10px}

  .payment{position:absolute;left:24px;top:44px;width:290px}
  .payment .body-copy{font-size:6.2px}
  .milestones{display:grid;grid-template-columns:1fr 1fr;margin:4px 0 0 0;width:200px}
  .milestones li{font-size:6.2px}
  .budget-table{position:absolute;left:24px;top:120px;width:292px;height:150px;border-collapse:collapse}
  .budget-table td{border:1px solid var(--rule)}
  .services{position:absolute;left:24px;top:290px;width:292px}
  .services__lead{font-size:7px;font-weight:700;color:var(--ink);margin-bottom:2px}
  .service-list{list-style:none;display:grid;grid-template-columns:1fr 1fr;row-gap:10px;margin-top:12px}
  .service-list li{display:flex;align-items:center;gap:6px;font-size:7px;color:var(--ink-soft)}
  .service-list svg{width:10px;height:10px;flex:none}
</style>
</head>
<body>

<svg width="0" height="0" style="position:absolute" aria-hidden="true">
  <defs>
    <symbol id="tick" viewBox="0 0 10 10"><rect x=".5" y=".5" width="9" height="9" fill="none" stroke="#8c1f26"/><path d="M2.3 5.2 4.2 7.1 7.9 2.8" fill="none" stroke="#8c1f26" stroke-width="1.4"/></symbol>
  </defs>
</svg>

<section class="spread spread--front">
  <article class="page back-cover">
    <div class="back-cover__photo" role="img" aria-label="Faded photo of film crew equipment and lighting rigs"></div>
    <svg class="shape-layer" viewBox="0 0 340 480" aria-hidden="true">
      <polygon points="22,0 250,0 160,215" fill="#8c1f26" opacity=".92"/>
      <polygon points="0,330 0,480 215,480" fill="#8c1f26" opacity=".92"/>
    </svg>
    <div class="brand"><span class="brand__dot"></span>Bright Marlow Films</div>
    <div class="contact">
      <div class="contact__title">CONTACT US:</div>
      <div class="contact__row">
        <svg class="contact__icon" viewBox="0 0 12 12"><circle cx="6" cy="6" r="5.5" fill="none" stroke="#8c1f26"/><path d="M6 3a2 2 0 0 0-2 2c0 1.5 2 3.8 2 3.8S8 6.5 8 5a2 2 0 0 0-2-2z" fill="#8c1f26"/></svg>
        <span>#210 - 48 Harbour Lane<br>Easton, BC</span>
      </div>
      <div class="contact__row">
        <svg class="contact__icon" viewBox="0 0 12 12"><circle cx="6" cy="6" r="5.5" fill="none" stroke="#8c1f26"/><path d="M4 3.2 5 3l.7 1.6-.7.6c.3.7.8 1.2 1.5 1.5l.6-.7L8.8 7l-.2 1c-2.6 0-4.8-2.2-4.6-4.8z" fill="#8c1f26"/></svg>
        <span>555.014.2290</span>
      </div>
      <div class="contact__row">
        <svg class="contact__icon" viewBox="0 0 12 12"><circle cx="6" cy="6" r="5.5" fill="none" stroke="#8c1f26"/><rect x="3.2" y="4" width="5.6" height="4" fill="none" stroke="#8c1f26" stroke-width=".8"/><path d="M3.2 4 6 6.2 8.8 4" fill="none" stroke="#8c1f26" stroke-width=".8"/></svg>
        <span>jordan@brightmarlowfilms.com</span>
      </div>
    </div>
  </article>

  <article class="page front-cover">
    <div class="front-cover__photo" role="img" aria-label="Photo of a professional cinema camera rig on set"></div>
    <div class="front-cover__header"></div>
    <svg class="shape-layer" viewBox="0 0 340 480" aria-hidden="true">
      <polygon points="0,215 340,292 340,480 0,480" fill="#2c2c30"/>
      <polygon points="340,110 340,300 222,270" fill="#8c1f26"/>
    </svg>
    <div class="brand"><span class="brand__dot"></span>Bright Marlow Films</div>
    <div class="cover-pitch">
      <h1 class="cover-pitch__title">Let's tell<br>your story<br>together</h1>
      <p class="cover-pitch__text">We collaborate to inform, educate and inspire your audience to create a movement.</p>
    </div>
    <div class="cover-url">www.brightmarlowfilms.com</div>
  </article>

  <div class="fold-tabs" aria-hidden="true">
    <span class="fold-tab" style="top:20px"></span>
    <span class="fold-tab" style="top:140px"></span>
    <span class="fold-tab" style="top:260px"></span>
    <span class="fold-tab" style="top:400px"></span>
  </div>
</section>
<div class="spread-label spread-label--front">Front</div>

<section class="spread spread--inside">
  <article class="page inside-page">
    <div class="brand"><span class="brand__dot"></span>Bright Marlow Films</div>
    <div class="overview">
      <h2 class="section-title">General Overview</h2>
      <p class="body-copy">At Bright Marlow Films, we take a creative, collaborative, planned approach to creating exceptional videos. We take you on a journey from start to finish, guiding you through the stages and removing the element of surprise. Our goal is to give you the peace of mind that we will tell your story with care. Here are the 4 stages that you can expect, with a breakdown of the time usually required at each stage.</p>

      <div class="stage">
        <h3 class="stage__title">Stage 1: Collaboration + Script development</h3>
        <ul class="tick-list">
          <li><svg class="tick"><use href="#tick"/></svg><span><b>Our role:</b> we seek to understand the call to action, the audience, your goals and your brand, then draft a script to fit.</span></li>
          <li><svg class="tick"><use href="#tick"/></svg><span><b>Your role:</b> act as a collaborator, share information and feedback to help us refine your ideas.</span></li>
        </ul>
        <p class="stage__note">(This stage accounts for approx. 40 % of the overall project time)</p>
      </div>
      <div class="stage">
        <h3 class="stage__title">Stage 2: Pre-production</h3>
        <ul class="tick-list">
          <li><svg class="tick"><use href="#tick"/></svg><span><b>Our role:</b> in preparation for the shoot, handle logistics, locations, equipment rentals, crew, talent and props.</span></li>
          <li><svg class="tick"><use href="#tick"/></svg><span><b>Your role:</b> if applicable, liaise with talent and organize locations together with our team.</span></li>
        </ul>
        <p class="stage__note">(This stage accounts for approx. 15 % of the overall project time)</p>
      </div>
      <div class="stage">
        <h3 class="stage__title">Stage 3: Filming</h3>
        <ul class="tick-list">
          <li><svg class="tick"><use href="#tick"/></svg><span><b>Our role:</b> directing and filming, managing all on-site parties, coaching talent and crew.</span></li>
          <li><svg class="tick"><use href="#tick"/></svg><span><b>Your role:</b> attend as needed to ensure the messaging stays on point.</span></li>
        </ul>
        <p class="stage__note">(This stage accounts for approx. 15 % of the overall project time)</p>
      </div>
      <div class="stage">
        <h3 class="stage__title">Stage 4: Editing</h3>
        <ul class="tick-list">
          <li><svg class="tick"><use href="#tick"/></svg><span><b>Our role:</b> cutting the raw footage into a compelling, concise finished product in line with the final script.</span></li>
          <li><svg class="tick"><use href="#tick"/></svg><span><b>Your role:</b> review two screenings included in the quote. All feedback is captured and addressed.</span></li>
        </ul>
        <p class="stage__note">(This stage accounts for approx. 30 % of the overall project time)</p>
      </div>
    </div>
    <div class="page-url">www.brightmarlowfilms.com</div>
  </article>

  <article class="page inside-page">
    <div class="brand"><span class="brand__dot"></span>Bright Marlow Films</div>
    <div class="payment">
      <h2 class="section-title">Payment process:</h2>
      <p class="body-copy">For projects under 30 days, payment is due upon project completion.<br><b>For projects over 30 days, we invoice at the following milestones:</b></p>
      <ul class="tick-list milestones">
        <li><svg class="tick"><use href="#tick"/></svg>upon script approval</li>
        <li><svg class="tick"><use href="#tick"/></svg>upon shoot completion</li>
        <li><svg class="tick"><use href="#tick"/></svg>prior to pre-production</li>
        <li><svg class="tick"><use href="#tick"/></svg>after 2 screenings</li>
      </ul>
    </div>
    <table class="budget-table" aria-label="Budget table">
      <tr><td></td><td></td><td></td><td></td><td></td><td></td></tr>
      <tr><td></td><td></td><td></td><td></td><td></td><td></td></tr>
      <tr><td></td><td></td><td></td><td></td><td></td><td></td></tr>
      <tr><td></td><td></td><td></td><td></td><td></td><td></td></tr>
      <tr><td></td><td></td><td></td><td></td><td></td><td></td></tr>
      <tr><td></td><td></td><td></td><td></td><td></td><td></td></tr>
      <tr><td></td><td></td><td></td><td></td><td></td><td></td></tr>
      <tr><td></td><td></td><td></td><td></td><td></td><td></td></tr>
    </table>
    <div class="services">
      <h2 class="section-title">Services</h2>
      <p class="services__lead">Telling a story that people want to be part of.</p>
      <p class="body-copy">Whether you're looking for bite-sized, searchable content for social media channels or a longer-form documentary, we take a general concept and create a reality that aligns with your ideal outcome. We lead the entire process collaboratively, from ideation through to the final reveal.</p>
      <ul class="service-list">
        <li><svg viewBox="0 0 10 10"><path d="M6 0 1.5 5.5H5L3.8 10 8.5 4H5z" fill="#8c1f26"/></svg>Creative Concepts</li>
        <li><svg viewBox="0 0 10 10"><path d="M1 1h6v8H1zM7 1h2v2H7z" fill="#8c1f26"/></svg>Script Development</li>
        <li><svg viewBox="0 0 10 10"><rect x=".5" y="2" width="7" height="6" fill="#8c1f26"/><path d="M7.5 5 9.5 3v4z" fill="#8c1f26"/></svg>UltraHD Production</li>
        <li><svg viewBox="0 0 10 10"><rect x="0" y="4" width="7" height="5" fill="#8c1f26"/><rect x="2.5" y="1" width="7" height="5" fill="none" stroke="#8c1f26"/></svg>Editing &amp; Motion Graphics</li>
      </ul>
    </div>
    <div class="page-url">www.brightmarlowfilms.com</div>
  </article>

  <div class="fold-tabs" aria-hidden="true">
    <span class="fold-tab" style="top:20px"></span>
    <span class="fold-tab" style="top:150px"></span>
    <span class="fold-tab" style="top:300px"></span>
    <span class="fold-tab" style="top:430px"></span>
  </div>
</section>
<div class="spread-label spread-label--inside">Inside</div>

</body>
</html>
```